Bar and Grill needs specials signage

I have attached a file called "daily specials" I need it changed - so there is 1 sign/poster for each day/special
also attached other items to show some styling. I want the new posters chalkboard format, styled along the lines of the drink designs attached.
The designs should be scaleable, and editable, I will print locally

```html
<!DOCTYPE html>
<html lang="en">
<head>
<meta charset="utf-8">
<title>Monday Daily Special</title>
<link rel="stylesheet" href="https://fonts.googleapis.com/css2?family=Oswald:wght@400&family=Lobster+Two:wght@700&family=Alegreya+Sans:wght@400&display=swap">
<style>
  :root {
    --board: #2b2b2b;
    --board-light: #383838;
    --board-dark: #1c1c1c;
    --chalk: #e2e2e2;
    --chalk-soft: #bdbdbd;
    --chalk-line: #a9a9a9;
    --accent: #f07e22;
  }
  html, body {
    margin: 0;
    padding: 0;
    width: 927px;
    height: 1200px;
    overflow: hidden;
    background: var(--board-dark);
  }
  .poster {
    position: relative;
    width: 927px;
    height: 1200px;
    background: radial-gradient(ellipse at 50% 40%, var(--board-light) 0%, var(--board) 55%, var(--board-dark) 100%);
    overflow: hidden;
  }
  .frame {
    position: absolute;
    inset: 10px;
    border: 2px solid var(--chalk-line);
    opacity: .75;
  }
  .frame::after {
    content: "";
    position: absolute;
    inset: 4px;
    border: 1px solid var(--chalk-line);
    opacity: .6;
  }
  .contact-card {
    position: absolute;
    left: 346px;
    top: 34px;
    width: 236px;
    height: 236px;
    border: 2px solid var(--chalk-line);
    box-sizing: border-box;
    text-align: center;
    font-family: "Oswald", sans-serif;
    color: var(--chalk-soft);
  }
  .contact-card::after {
    content: "";
    position: absolute;
    inset: 4px;
    border: 1px solid var(--chalk-line);
    opacity: .6;
  }
  .brand-square {
    position: absolute;
    left: 60px;
    top: -4px;
    width: 112px;
    height: 98px;
    background: var(--accent);
  }
  .contact-name {
    position: absolute;
    top: 100px;
    left: 0;
    right: 0;
    font-size: 33px;
    line-height: 1;
    letter-spacing: -.5px;
  }
  .contact-email, .contact-phone, .contact-address {
    position: absolute;
    left: 0;
    right: 0;
    line-height: 1;
  }
  .contact-email { top: 143px; font-size: 13.5px; letter-spacing: -.2px; }
  .contact-phone { top: 166px; font-size: 15px; }
  .contact-address { top: 186px; font-size: 11px; line-height: 1.3; }
  .headline {
    position: absolute;
    top: 318px;
    left: 0;
    right: 0;
    margin: 0;
    text-align: center;
    font-family: "Lobster Two", cursive;
    font-weight: 700;
    font-size: 92px;
    line-height: 118px;
    color: var(--chalk);
  }
  .divider {
    position: absolute;
    left: 160px;
    width: 596px;
    height: 0;
    border-top: 3px dotted var(--chalk-line);
    opacity: .8;
  }
  .divider--top { top: 608px; }
  .divider--bottom { top: 1126px; }
  .offer {
    position: absolute;
    top: 630px;
    left: 0;
    right: 0;
    margin: 0;
    text-align: center;
    font-family: "Alegreya Sans", sans-serif;
    font-size: 78px;
    line-height: 110px;
    color: var(--chalk-soft);
  }
</style>
</head>
<body>
  <main class="poster">
    <div class="frame"></div>

    <header class="contact-card">
      <div class="brand-square"></div>
      <div class="contact-name">DANA WHITFIELD</div>
      <div class="contact-email">FAIRVIEW@OAKANDEMBER.COM</div>
      <div class="contact-phone">555-014-7290</div>
      <div class="contact-address">1842 ELM RIDGE<br>FAIRVIEW, MISSOURI 63000</div>
    </header>

    <h1 class="headline">Monday<br>daily special</h1>

    <div class="divider divider--top"></div>

    <p class="offer">kids eat free<br>from our<br>kids menu, with<br>adult purchase</p>

    <div class="divider divider--bottom"></div>
  </main>
</body>
</html>
```